Quorvex - Automated robotic Inspection with AI need new business cards

We need a new design of our business cards. The company is focused on automated quality control at high speed with unmatched results. We have a logo but need a more forward leaning business card that shows that we are delivering cutting edge technology.

Contact Information for Business Card

Name
Position
Adress
Phone
Email
e.g.
Lena Holmqvist
Chief Financial Officer (CFO)

Quorvex Sweden AB
Bruksvägen 14, SE-175 43 JÄRFÄLLA, Sweden
Mobile: +46735 21 47 83 | Office: +46 8 61 94 27
www.quorvex-example.com

Font styles to use
Sans Serif

```html
<!DOCTYPE html>
<html lang="en">
<head>
<meta charset="utf-8">
<title>Quorvex business card</title>
<link rel="stylesheet" href="https://fonts.googleapis.com/css2?family=Arimo:wght@400;700&display=swap">
<style>
  :root {
    --brand-blue: #15507f;
    --brand-blue-light: #1b5d92;
    --paper: #f4f4f4;
    --sweep-grey: #9a9a9a;
    --ink: #1e1e1e;
    --on-blue: #ffffff;
    --logo-grey: #dcdcdc;
    --backdrop: #2a2a2a;
  }
  * { margin: 0; padding: 0; box-sizing: border-box; }
  html, body { width: 1200px; height: 900px; overflow: hidden; }
  body {
    background: var(--backdrop);
    font-family: "Arimo", Arial, sans-serif;
    display: flex;
    flex-direction: column;
    align-items: center;
    justify-content: center;
    gap: 40px;
  }
  .card {
    position: relative;
    width: 700px;
    height: 400px;
    overflow: hidden;
    box-shadow: 0 10px 30px rgba(0,0,0,.5);
  }
  .card-front { background: var(--paper); }
  .front-sweep { position: absolute; inset: 0; width: 100%; height: 100%; }
  .wordmark {
    position: absolute;
    display: flex;
    align-items: center;
    gap: 14px;
    font-weight: 700;
    letter-spacing: 2px;
  }
  .card-front .wordmark { left: 48px; top: 38px; color: var(--brand-blue); font-size: 44px; }
  .wordmark-dot { width: 30px; height: 30px; border-radius: 50%; background: currentColor; }
  .person { position: absolute; left: 48px; top: 112px; }
  .person-name { color: var(--brand-blue); font-weight: 700; font-size: 24px; letter-spacing: 1px; text-transform: uppercase; }
  .person-title { color: var(--ink); font-size: 16px; margin-top: 4px; }
  .company-address {
    position: absolute; right: 40px; top: 236px;
    color: var(--on-blue); text-align: right; font-size: 14px; line-height: 1.35;
  }
  .contact-list {
    position: absolute; right: 40px; bottom: 26px;
    list-style: none; color: var(--on-blue); font-size: 14px; line-height: 1.45;
  }
  .contact-list li { display: flex; justify-content: flex-end; align-items: center; gap: 8px; }
  .contact-list svg { width: 13px; height: 13px; fill: var(--on-blue); }
  .card-back {
    background: radial-gradient(ellipse 70% 40% at 50% 48%, var(--brand-blue-light), var(--brand-blue) 75%);
  }
  .card-back .wordmark {
    left: 0; right: 0; top: 150px; justify-content: center;
    color: var(--logo-grey); font-size: 72px; letter-spacing: 4px;
  }
  .card-back .wordmark-dot { width: 44px; height: 44px; }
  .back-url {
    position: absolute; left: 0; right: 0; top: 262px;
    text-align: center; color: var(--logo-grey); font-size: 18px;
  }
</style>
</head>
<body>
  <section class="card card-front">
    <svg class="front-sweep" viewBox="0 0 700 400" preserveAspectRatio="none" aria-hidden="true">
      <path d="M0 148 Q330 250 700 232 L700 400 L0 400 Z" fill="var(--sweep-grey)"/>
      <path d="M0 156 Q330 262 700 252 L700 400 L0 400 Z" fill="var(--brand-blue)"/>
    </svg>
    <div class="wordmark"><span class="wordmark-dot"></span>QUORVEX</div>
    <div class="person">
      <p class="person-name">Lena Holmqvist</p>
      <p class="person-title">Chief Financial Officer (CFO)</p>
    </div>
    <address class="company-address" style="font-style:normal">
      Quorvex Sweden AB<br>
      Bruksvägen 14, SE-175 43<br>
      JÄRFÄLLA, Sweden
    </address>
    <ul class="contact-list">
      <li>+46 8 61 94 27
        <svg viewBox="0 0 24 24"><path d="M6.6 10.8a15 15 0 0 0 6.6 6.6l2.2-2.2a1 1 0 0 1 1-.25 11.4 11.4 0 0 0 3.6.57 1 1 0 0 1 1 1V20a1 1 0 0 1-1 1A17 17 0 0 1 3 4a1 1 0 0 1 1-1h3.5a1 1 0 0 1 1 1c0 1.25.2 2.45.57 3.6a1 1 0 0 1-.25 1z"/></svg></li>
      <li>+46735 21 47 83
        <svg viewBox="0 0 24 24"><path d="M7 1h10a2 2 0 0 1 2 2v18a2 2 0 0 1-2 2H7a2 2 0 0 1-2-2V3a2 2 0 0 1 2-2zm0 3v14h10V4zm5 15.5a1 1 0 1 0 0 2 1 1 0 0 0 0-2z"/></svg></li>
      <li>lena.holmqvist@quorvex-example.com
        <svg viewBox="0 0 24 24"><path d="M2 5h20v14H2zm2 2v.5l8 5 8-5V7zm0 3v7h16v-7l-8 5z"/></svg></li>
      <li>www.quorvex-example.com
        <svg viewBox="0 0 24 24"><path d="M12 2a10 10 0 1 0 0 20 10 10 0 0 0 0-20zm-1 2.1V8H7.3A8 8 0 0 1 11 4.1zm2 0A8 8 0 0 1 16.7 8H13zM6.3 10H11v4H6.3a8 8 0 0 1 0-4zm6.7 0h4.7a8 8 0 0 1 0 4H13zm-5.7 6H11v3.9A8 8 0 0 1 7.3 16zm5.7 0h3.7a8 8 0 0 1-3.7 3.9z"/></svg></li>
    </ul>
  </section>

  <section class="card card-back">
    <div class="wordmark"><span class="wordmark-dot"></span>QUORVEX</div>
    <p class="back-url">www.quorvex-example.com</p>
  </section>
</body>
</html>
```